Zielgruppe
Zeitarbeit Personalvermittlung Arbeitsvermittlung Arbeitnehmerüberlassung
Zielgruppe:
Akademiker
Fachkräfte
Politiker
Ingenieur
wichtige Akteure der Gesellschaft
Kommunen
Vereinigungen
Aufgabenstellung
Wir benötigen schlichte und dezente, aber eindrucksvolle,exklusive Visitenkarten mit unserem Logo.
Aufbau:
Vorname, Name
Position
Telefon
Mobil
E-Mail
Fax
Unsere Website: http://www.velmaris-personal.de
Wir sind 2 Geschäftsführer also bitte für beide Namen
Dies benötigen wir als PSD, PDF, JPG, sodass wir selbst die Angaben nach Belieben eintragen können.

```html
<!DOCTYPE html>
<html lang="de">
<head>
<meta charset="utf-8">
<title>Velmaris Visitenkarten</title>
<link href="https://fonts.googleapis.com/css2?family=Open+Sans:wght@300;400;600;700&display=swap" rel="stylesheet">
<style>
  :root {
    --bg: #ebebeb;
    --paper: #ffffff;
    --charcoal: #36393b;
    --orange: #f08a0c;
    --ink: #3a3a3a;
    --rule: #8a8a8a;
    --muted: #9a9a9a;
  }
  html, body {
    margin: 0;
    width: 1200px;
    height: 800px;
    overflow: hidden;
    background: var(--bg);
    font-family: "Open Sans", Arial, sans-serif;
  }
  .canvas {
    position: relative;
    width: 1200px;
    height: 800px;
  }
  .card {
    position: absolute;
    top: 250px;
    width: 480px;
    height: 300px;
    box-sizing: border-box;
    overflow: hidden;
  }
  .card--front { left: 90px; background: var(--paper); }
  .card--back { left: 630px; background: var(--charcoal); }

  .brand { position: absolute; display: flex; align-items: center; gap: 12px; }
  .brand__mark { width: 22px; height: 22px; background: var(--orange); flex: none; }
  .brand__text { display: flex; flex-direction: column; }
  .brand__name { font-weight: 300; line-height: 1; letter-spacing: 0.5px; }
  .brand__tagline { font-weight: 300; text-transform: uppercase; }

  .card--front .brand { left: 34px; top: 34px; }
  .card--front .brand__name { font-size: 36px; color: var(--ink); }
  .card--front .brand__tagline { font-size: 6.5px; letter-spacing: 3.4px; color: var(--muted); margin-top: 4px; }
  .front__rule-top {
    position: absolute; left: 258px; right: 34px; top: 46px;
    height: 1px; background: var(--rule);
  }

  .person { position: absolute; left: 160px; top: 100px; }
  .person__name { font-size: 15px; font-weight: 700; color: var(--ink); margin: 0; }
  .person__role { font-size: 12px; color: var(--ink); margin: 0; }
  .front__rule-mid {
    position: absolute; left: 34px; width: 250px; top: 146px;
    height: 1px; background: var(--rule);
  }

  .address { position: absolute; left: 160px; top: 154px; font-size: 9.5px; line-height: 1.35; color: var(--ink); }
  .address strong { font-weight: 700; }
  .contact { position: absolute; left: 160px; top: 206px; font-size: 9.5px; line-height: 1.45; color: var(--ink); }
  .contact .label { color: var(--orange); font-weight: 600; }

  .front__band {
    position: absolute; left: 0; right: 0; bottom: 0; height: 34px;
    background: var(--orange);
    display: flex; align-items: center; justify-content: flex-end;
    padding-right: 34px;
  }
  .front__website { color: #fff; font-size: 10.5px; }

  .card--back .brand { left: 110px; top: 118px; gap: 16px; }
  .card--back .brand__mark { width: 34px; height: 34px; }
  .card--back .brand__name { font-size: 52px; color: #fff; }
  .card--back .brand__tagline { font-size: 7.5px; letter-spacing: 5px; color: #e6e6e6; margin-top: 6px; }
</style>
</head>
<body>
<main class="canvas">

  <section class="card card--front" aria-label="Visitenkarte Vorderseite">
    <div class="brand">
      <span class="brand__mark"></span>
      <div class="brand__text">
        <span class="brand__name">velmaris</span>
        <span class="brand__tagline">Personaldienstleistungen</span>
      </div>
    </div>
    <div class="front__rule-top"></div>

    <div class="person">
      <p class="person__name">Lukas Herrmann</p>
      <p class="person__role">Geschäftsführer</p>
    </div>
    <div class="front__rule-mid"></div>

    <div class="address">
      <strong>velmaris</strong> Personaldienstleistungen<br>
      Lindenallee 22<br>
      68159 Mannheim
    </div>

    <div class="contact">
      <span class="label">Fon:</span> +49(0) 30 55 21 80 | <span class="label">Fax:</span> +49(0) 30 55 21 81<br>
      <span class="label">Mobil:</span> +49(0) 171 48 29 03 | <span class="label">Mail:</span> herrmann@velmaris-personal.de
    </div>

    <div class="front__band">
      <span class="front__website">www.velmaris-personal.de</span>
    </div>
  </section>

  <section class="card card--back" aria-label="Visitenkarte Rückseite">
    <div class="brand">
      <span class="brand__mark"></span>
      <div class="brand__text">
        <span class="brand__name">velmaris</span>
        <span class="brand__tagline">Personaldienstleistungen</span>
      </div>
    </div>
  </section>

</main>
</body>
</html>
```